Zielgruppe
Ich bin Selfpublisher und habe eine Mondschein Merkheft als Buch kreiert. Die Zielgruppe sind meist junge Erwachsene, aber auch welche mittleren alters.
Aufgabenstellung
Titel des Buches: Das geheime MONDSCHEIN MERKHEFT
Untertitel: 150 Orte +10 eigene Orte für mehr Nervenkitzel und Erlebnisse
Der Anfang vom Titel 'Die große' kann ruhig sehr klein abgebildet werden.
Das Wort 'SEX' im Titel soll am größten auf dem Cover sein und auch bei kleinster Darstellung gut sichtbar und sehr prägnant sein.
Der Teil vom Untertitel '+10 eigene Orte für mehr Nervenkitzel und Erlebnisse' kann ruhig getrennt von den '150 Orten' stehen.
In dem Buch sind 150 Orte plus jeweils Felder zum Ankreuzen und beschreiben vorhanden, wie der Sex dort war.
Farben: Die Hauptfarbe soll ins rote gehen.
Auf keinen Fall darf dieses Rot #EE3A43 benutzt werden, da dies die Farbe eines Mitbewerbers ist.
Hier zwei Beispiele welche Farben benutzt werden können: #FF4D8D, #FF6686. Natürlich sind auch andere und ähnliche Farben in Ordnung. Dies diente nur zur Orientierung, wie weit das Rot verändert werden muss.
Es sollen keine echten Fotos verwendet werden. Außerdem sollen keine Menschen, oder Illustrationen von Menschen abgebildet werden.
Ich habe eine Datei hochgeladen, worin sich mehrere Illustrationen befinden. Die können in der Farbe und vom Aussehen verändert werden. Das benutzen der Illustrationen ist absolut kein muss! Ich lasse mich gerne von anderen Designs überraschen.
Mit den Illustrationen könnte man zum Beispiel sowas wie auf dem Cover der 'Ferien Rätselheft' abgebildet machen. Bild ist im Anhang. Hierfür müssen die Illustrationen (Sex Icons) mit passenden Farben versehen werden. Es sollte nicht zu Bunt werden, also hier 3-4 Farben aussuchen.
Außerdem eventuell ein Schrift Effekt wie bei dem Titel der 'Harbor Riddles' auch im Anhang zu finden. Natürlich gehen auch andere passende Effekte. Hier kenne ich mich nicht aus, was so möglich ist.
Es sollte allgemein nicht zu langweilig sein. Etwas Dynamik und Effekte sind gut. Wie bei den bereits genannten Beispiel Covern.

```html
<!DOCTYPE html>
<html lang="de">
<head>
<meta charset="utf-8">
<title>Das geheime Mondschein Merkheft – Cover</title>
<link rel="stylesheet" href="https://fonts.googleapis.com/css2?family=Luckiest+Guy&family=Barlow+Condensed:wght@700&display=block">
<style>
  :root {
    --stage: #f94c8c;
    --cover-light: #f9cddd;
    --cover-mid: #f5b6cc;
    --blob: #f7c0d3;
    --hot-pink: #f9508f;
    --deep-pink: #e93e7f;
    --white: #ffffff;
    --wine: #5a0a2a;
    --yellow: #ffbf00;
    --shadow: #8a1140;
    --display: "Luckiest Guy", "Arial Black", "Impact", sans-serif;
    --condensed: "Barlow Condensed", "Arial Narrow", sans-serif;
  }
  * { margin: 0; padding: 0; box-sizing: border-box; }
  html, body {
    width: 1200px;
    height: 2317px;
    overflow: hidden;
    background: var(--stage);
  }
  .cover {
    position: absolute;
    left: 100px;
    top: 433px;
    width: 1000px;
    height: 1450px;
    overflow: hidden;
    background: var(--cover-light);
  }
  .backdrop { position: absolute; inset: 0; }
  .tilted-panel {
    position: absolute;
    left: 70px;
    top: 250px;
    width: 900px;
    height: 700px;
    background: var(--hot-pink);
    transform: rotate(-4deg);
  }
  .kicker {
    position: absolute;
    left: 270px;
    top: 60px;
    padding: 12px 30px 4px;
    background: var(--yellow);
    transform: rotate(-5deg);
    font-family: var(--display);
    font-weight: 900;
    font-size: 58px;
    line-height: 1;
    color: var(--hot-pink);
    letter-spacing: 1px;
  }
  .title-main {
    position: absolute;
    left: 0;
    width: 1000px;
    top: 320px;
    text-align: center;
    font-family: var(--display);
    font-weight: 900;
    font-size: 104px;
    line-height: 1;
    color: var(--white);
    letter-spacing: -2px;
    white-space: nowrap;
    transform: rotate(-3deg) scaleY(2.5);
    -webkit-text-stroke: 10px var(--hot-pink);
    paint-order: stroke fill;
    text-shadow: 5px 3px 0 var(--shadow);
  }
  .title-sub {
    position: absolute;
    left: 0;
    width: 1000px;
    top: 620px;
    text-align: center;
    font-family: var(--display);
    font-weight: 900;
    font-size: 138px;
    line-height: 1;
    color: var(--white);
    white-space: nowrap;
    transform: rotate(-6deg) scaleY(1.3);
    -webkit-text-stroke: 10px var(--hot-pink);
    paint-order: stroke fill;
    text-shadow: 5px 5px 0 var(--shadow);
  }
  .count-tag {
    position: absolute;
    left: 325px;
    top: 880px;
    width: 410px;
    height: 105px;
    background: var(--wine);
    transform: rotate(-4deg);
    display: flex;
    align-items: center;
    justify-content: center;
    font-family: var(--condensed);
    font-weight: 700;
    font-size: 80px;
    color: var(--white);
  }
  .tagline {
    position: absolute;
    left: 0;
    width: 1000px;
    top: 1070px;
    text-align: center;
    font-family: var(--condensed);
    font-weight: 700;
    font-size: 52px;
    line-height: 1.05;
    color: var(--wine);
    letter-spacing: 1px;
  }
  .art {
    position: absolute;
    border-radius: 40%;
    background: var(--deep-pink);
    border: 6px solid var(--white);
  }
  .art-mask { left: 10px; top: 60px; width: 270px; height: 140px; transform: rotate(-10deg); }
  .art-heel { left: 775px; top: 850px; width: 170px; height: 175px; }
  .art-plug { left: 70px; top: 1280px; width: 140px; height: 140px; }
  .art-lips { left: 345px; top: 1215px; width: 300px; height: 165px; }
  .art-tv { left: 740px; top: 1225px; width: 200px; height: 185px; border-radius: 22px; }
</style>
</head>
<body>
  <main class="cover">
    <svg class="backdrop" width="1000" height="1450" viewBox="0 0 1000 1450" aria-hidden="true">
      <path d="M0 0 H1000 V180 C820 120 620 40 480 0 Z" fill="#fbd8e5"/>
      <path d="M0 980 C160 900 360 980 430 1120 C480 1230 380 1380 240 1450 H0 Z" fill="var(--blob)"/>
      <path d="M1000 1050 C880 1080 760 1180 780 1320 L800 1450 H1000 Z" fill="var(--cover-mid)"/>
      <circle cx="800" cy="60" r="14" fill="var(--hot-pink)"/>
      <circle cx="910" cy="130" r="22" fill="var(--hot-pink)"/>
      <circle cx="910" cy="330" r="20" fill="var(--cover-light)"/>
      <circle cx="865" cy="460" r="6" fill="var(--cover-light)"/>
      <circle cx="250" cy="1258" r="10" fill="var(--hot-pink)"/>
      <circle cx="300" cy="1335" r="24" fill="var(--hot-pink)"/>
      <circle cx="775" cy="1175" r="12" fill="var(--hot-pink)"/>
      <circle cx="695" cy="1230" r="7" fill="var(--hot-pink)"/>
    </svg>

    <div class="tilted-panel"></div>

    <div class="art art-mask" role="img" aria-label="Illustration: Maske"></div>
    <div class="kicker">DAS GEHEIME</div>

    <h1 class="title-main">MONDSCHEIN</h1>
    <div class="title-sub">MERKHEFT</div>

    <div class="count-tag">150 ORTE</div>
    <div class="art art-heel" role="img" aria-label="Illustration: High Heel"></div>

    <p class="tagline">+10 EIGENE ORTE FÜR MEHR<br>NERVENKITZEL UND ERLEBNISSE</p>

    <div class="art art-plug" role="img" aria-label="Illustration: Spielzeug"></div>
    <div class="art art-lips" role="img" aria-label="Illustration: Lippen"></div>
    <div class="art art-tv" role="img" aria-label="Illustration: Fernseher"></div>
  </main>
</body>
</html>
```